design an app for runners to engage them in collective challenges

Creative Brief: Running Application - Collective Challenges
Objective
To design a simple yet impactful mobile application for runners, centered around collective challenges. The app should offer an engaging, user-friendly experience while encouraging participation in running challenges. Starting with a minimalist and robust version, the design must focus on essential features, allowing for future enhancements as the user base grows.

Target Audience
Primary Users: Casual to dedicated runners who enjoy tracking their progress and participating in challenges.
Motivations: Community-driven goals, personal achievements, and tangible rewards.
Needs: A visually appealing, straightforward interface with real-time progress tracking and clear challenge objectives.
Core Features
Main Screen: Current Challenge

Displays the active challenge with a title, visual, prize description, and countdown for kilometers remaining.
Prominent “Join” button for easy participation.
Quick access to challenge conditions (eg, most kilometers, fastest pace, random draw).
Challenge Details

Includes challenge rules, detailed prize information, and victory conditions.
Simplified text for clarity and engagement.
Past Challenges

Showcases previous challenges, total kilometers achieved, and winners.
Admin Section

Enables challenge creation with scheduling, descriptions, and victory criteria.
Minimalist design for ease of use.
Look and Feel
Visual Identity: Clean, modern, and energetic design reflecting the spirit of running and collective achievement.
Color Palette:
Vibrant primary colors: Blue and green for energy and motivation.
Accent colors: Orange or yellow for highlights, paired with a dark background for strong contrast.
Typography:
Sans-serif fonts like Lato or Montserrat for readability.
Bold, prominent numbers for key statistics like kilometers completed.
Icons and Graphics:
Minimalistic icons with light, functional animations (eg, a moving kilometer counter).
Clear, motivational visuals to support collective progress.
Tone and Style
Tone: Encouraging, community-focused, and goal-oriented.
Style: Minimalistic with a focus on clarity and user engagement.
References
Inspirations:
Tavro Stride Circle for its simplicity and modern interface.
Pellux for its community features and tracking precision.
Deliverables
Wireframes and UI designs for all key screens: login, current challenge, challenge details, past challenges, and admin panel.
Visual assets: icons, buttons, and animations.
A consistent design system to ensure scalability for future features.
Updates

Target Market(s)

Casual to dedicated runners who enjoy tracking their progress and participating in challenges.

Industry/Entity Type

sport

Font styles to use
Sans Serif

Colors

Designer to choose colors to be used in the design.

Requirements
Must have
• to design all screens

```html
<!DOCTYPE html>
<html lang="en">
<head>
<meta charset="utf-8">
<title>Run Challenges – App Screens</title>
<link href="https://fonts.googleapis.com/css2?family=Exo+2:wght@400;500;600;700;800&display=swap" rel="stylesheet">
<style>
:root{
  --stage:#575757;
  --screen:#121212;
  --panel:#2a2a2a;
  --panel-2:#1e1e1e;
  --lime:#9ded12;
  --pale:#d8efab;
  --yellow:#f2d21b;
  --white:#ffffff;
  --muted:#a8a8a8;
  --ink:#111111;
}
*{box-sizing:border-box;margin:0;padding:0}
html,body{width:1091px;height:1200px;overflow:hidden}
body{background:var(--stage);font-family:"Exo 2",sans-serif;color:var(--white);position:relative}
.screen{position:absolute;width:388px;height:828px;background:var(--screen);border-radius:40px;overflow:hidden;transform:scale(.595);transform-origin:0 0}
.screen.tall{height:930px}
.abs{position:absolute}
.status{left:40px;top:20px;font-size:15px;font-weight:600}
.status-icons{right:34px;top:24px;display:flex;gap:5px}
.avatar{left:14px;top:58px;width:58px;height:44px;border-radius:50%;border:2px solid var(--lime);background:radial-gradient(circle at 50% 45%,#8a6d55,#3b4a5c 70%)}
.greet{left:80px;top:64px;font-size:13px;line-height:22px}
.greet b{font-weight:600;font-size:14px}
.greet .sub{color:var(--lime);font-weight:500}
.bell{right:16px;top:60px;width:50px;height:38px;border-radius:18px;border:1px solid #333;display:flex;align-items:center;justify-content:center}
.bell::after{content:"";position:absolute;right:-2px;top:-3px;width:10px;height:10px;border-radius:50%;background:var(--yellow);border:2px solid var(--screen)}
.section{left:14px;right:14px;display:flex;justify-content:space-between;align-items:center}
.section h2{font-size:19px;font-weight:600;letter-spacing:.3px}
.section h2 .slash{color:var(--lime);margin-right:6px}
.section .all{font-size:12px;color:var(--muted);letter-spacing:.4px}
.hero{left:7px;width:374px;height:176px;background:var(--lime);border-radius:18px 18px 0 0;overflow:hidden;color:var(--ink)}
.hero h3{position:absolute;left:29px;top:22px;font-size:22px;font-weight:700;line-height:26px}
.hero .trophy{position:absolute;left:29px;top:92px}
.hero .prize{position:absolute;left:29px;top:118px;font-size:13px;line-height:17px;width:170px}
.photo{position:absolute;right:0;top:0;bottom:0;width:165px;clip-path:polygon(38% 0,100% 0,100% 100%,0 100%)}
.photo.runner{background:linear-gradient(160deg,#5a6470 0%,#c9a236 45%,#e4c43a 60%,#2d3d8c 100%)}
.photo.pair{background:linear-gradient(150deg,#9aa8c0 0%,#e9e2d8 40%,#c44a3a 75%,#2c4f9e 100%)}
.photo.crowd{background:linear-gradient(160deg,#64707e 0%,#2b3f92 45%,#b84640 75%,#dcc9a8 100%)}
.pill{position:absolute;right:7px;bottom:8px;width:132px;height:34px;border-radius:17px;background:var(--pale);display:flex;align-items:center;justify-content:space-between;padding:0 14px;font-size:11px;font-weight:500;color:var(--ink)}
.togo{left:7px;width:374px;height:58px;background:var(--panel);border-radius:0 0 18px 18px;display:flex;align-items:center;padding:0 12px 0 30px}
.big{font-size:36px;font-weight:800;margin-left:10px;letter-spacing:-.5px}
.unit{font-size:13px;font-weight:600;line-height:11px;margin-left:6px}
.unit small{display:block;font-size:10px;font-weight:500}
.join{margin-left:auto;font-size:13px;font-weight:600;color:var(--yellow);letter-spacing:.3px}
.circle-btn{width:50px;height:36px;border-radius:18px;border:1.5px solid var(--yellow);display:flex;align-items:center;justify-content:center;margin-left:8px}
.stats{left:7px;width:374px;height:124px;background:var(--pale);color:var(--ink)}
.stat{position:absolute;top:22px}
.stat .n{font-size:36px;font-weight:800;margin-top:6px;line-height:40px}
.stat .n sup{font-size:13px;font-weight:600;vertical-align:18px;margin-left:4px}
.stat .l{font-size:11px;font-weight:500;margin-top:2px}
.event{left:7px;width:374px;height:80px;background:var(--panel);border-radius:14px;overflow:hidden}
.event .date{position:absolute;left:28px;top:20px;font-size:21px;font-weight:800;line-height:20px}
.event .date small{display:block;font-size:14px;font-weight:600}
.event .date.soon{color:var(--yellow)}
.event .info{position:absolute;left:74px;right:0;top:0;bottom:0;background:var(--pale);clip-path:polygon(28px 0,100% 0,100% 100%,0 100%);color:var(--ink)}
.event h4{position:absolute;left:36px;top:14px;font-size:16px;font-weight:600}
.event .dist{position:absolute;left:36px;top:44px;font-size:12px;display:flex;align-items:center;gap:6px}
.event .check{position:absolute;right:18px;top:50px;font-size:12px;font-weight:500;display:flex;align-items:center;gap:8px}
.fab{width:66px;height:50px;border-radius:16px;background:var(--lime);display:flex;align-items:center;justify-content:center;left:308px}
.create{left:14px;font-size:19px;font-weight:600}
.create .plus{color:var(--lime)}
.clan{left:7px;width:374px;height:176px;border-radius:18px;overflow:hidden;background:#a9d932;color:var(--ink)}
.clan h3{position:absolute;left:29px;top:22px;font-size:22px;font-weight:700;line-height:26px}
.clan .prize-tag{position:absolute;left:29px;top:94px;font-size:11px;display:flex;align-items:center;gap:6px}
.clan .note{position:absolute;left:29px;top:120px;font-size:13px;line-height:17px}
.go{position:absolute;right:7px;bottom:8px;width:132px;height:34px;border-radius:17px;background:var(--lime);display:flex;align-items:center;justify-content:space-between;padding:0 14px;font-size:12px;font-weight:600}
.nav{left:22px;top:740px;width:346px;height:58px;border-radius:30px;background:rgba(36,36,36,.92);display:flex;align-items:center;gap:8px;padding:0 7px}
.nav .tab{height:44px;border-radius:22px;background:#333;display:flex;align-items:center;justify-content:center;flex:0 0 62px}
.nav .tab.wide{flex:0 0 128px;gap:10px;font-size:10px;font-weight:600;color:var(--yellow)}
.tabs{left:0;top:52px;width:388px;height:46px;background:#2e2e2e;font-size:13px;font-weight:500}
.tabs .past{position:absolute;left:36px;top:15px;color:var(--muted)}
.tabs .current{position:absolute;right:0;top:0;width:200px;height:46px;background:var(--screen);clip-path:polygon(18px 0,100% 0,100% 100%,0 100%);padding:15px 0 0 30px;font-weight:600}
.filter{top:118px;height:44px;border-radius:22px;border:1px solid #3a3a3a;display:flex;align-items:center;gap:10px;padding:0 14px;font-size:13px;font-weight:500}
</style>
</head>
<body>

<svg width="0" height="0" style="position:absolute">
  <defs>
    <symbol id="i-bell" viewBox="0 0 24 24"><path d="M6 17V11a6 6 0 0 1 12 0v6l1.5 2h-15z M10 21h4" fill="none" stroke="#f2d21b" stroke-width="1.8" stroke-linejoin="round"/></symbol>
    <symbol id="i-trophy" viewBox="0 0 24 24"><path d="M7 3h10v6a5 5 0 0 1-10 0z M7 5H3v2a4 4 0 0 0 4 4 M17 5h4v2a4 4 0 0 1-4 4 M12 14v4 M8 21h8 M9 18h6" fill="none" stroke="#111" stroke-width="1.6" stroke-linejoin="round"/></symbol>
    <symbol id="i-watch" viewBox="0 0 24 24"><circle cx="12" cy="13" r="8" fill="none" stroke="currentColor" stroke-width="1.8"/><path d="M12 13V9 M10 2h4" fill="none" stroke="currentColor" stroke-width="1.8" stroke-linecap="round"/></symbol>
    <symbol id="i-chev" viewBox="0 0 24 24"><path d="M10 7l5 5-5 5" fill="none" stroke="currentColor" stroke-width="2" stroke-linecap="round" stroke-linejoin="round"/></symbol>
    <symbol id="i-route" viewBox="0 0 24 24"><circle cx="7" cy="6" r="2.5" fill="none" stroke="#111" stroke-width="1.6"/><circle cx="18" cy="18" r="2.5" fill="none" stroke="#111" stroke-width="1.6"/><path d="M7 9v3h10 M4 16h9v4H3" fill="none" stroke="#111" stroke-width="1.6"/></symbol>
    <symbol id="i-bars" viewBox="0 0 24 24"><path d="M6 7v10 M12 4v16 M18 9v6" stroke="#111" stroke-width="2" stroke-linecap="round"/></symbol>
    <symbol id="i-close" viewBox="0 0 24 24"><path d="M6 6l12 12 M18 6L6 18" stroke="#111" stroke-width="1.8" stroke-linecap="round"/></symbol>
    <symbol id="i-alarm" viewBox="0 0 24 24"><circle cx="12" cy="13" r="7.5" fill="none" stroke="currentColor" stroke-width="1.7"/><path d="M12 10v6 M9 13h6 M3 6l3-3 M21 6l-3-3" stroke="currentColor" stroke-width="1.7" stroke-linecap="round"/></symbol>
    <symbol id="i-home" viewBox="0 0 24 24"><path d="M4 11l8-7 8 7v9H4z M10 20v-5h4v5" fill="none" stroke="currentColor" stroke-width="1.7" stroke-linejoin="round"/></symbol>
    <symbol id="i-grid" viewBox="0 0 24 24"><path d="M4 7h3v3H4z M10 7h3v3h-3z M16 7h3v3h-3z M7 10h3v3H7z M13 10h3v3h-3z M4 13h3v3H4z M10 13h3v3h-3z M16 13h3v3h-3z" fill="currentColor"/></symbol>
    <symbol id="i-slide" viewBox="0 0 24 24"><path d="M3 8h18 M3 16h18" stroke="currentColor" stroke-width="1.6"/><circle cx="9" cy="8" r="2.5" fill="#333" stroke="currentColor" stroke-width="1.6"/><circle cx="15" cy="16" r="2.5" fill="#333" stroke="currentColor" stroke-width="1.6"/></symbol>
    <symbol id="i-gauge" viewBox="0 0 24 24"><circle cx="12" cy="12" r="8.5" fill="none" stroke="#111" stroke-width="1.6"/><path d="M12 13l4-5" stroke="#111" stroke-width="1.8" stroke-linecap="round"/></symbol>
    <symbol id="i-ticket" viewBox="0 0 24 24"><path d="M3 6h18v4a2 2 0 0 0 0 4v4H3v-4a2 2 0 0 0 0-4z" fill="none" stroke="#111" stroke-width="1.6" stroke-linejoin="round"/></symbol>
    <symbol id="i-trend" viewBox="0 0 24 24"><path d="M3 15c3-6 5-6 8-2s5 4 10-3" fill="none" stroke="#111" stroke-width="1.7" stroke-linecap="round"/></symbol>
    <symbol id="i-hour" viewBox="0 0 24 24"><path d="M7 3h10 M7 21h10 M8 3c0 5 8 5 8 9s-8 4-8 9 M16 3c0 5-8 5-8 9s8 4 8 9" fill="none" stroke="#f2d21b" stroke-width="1.7"/></symbol>
    <symbol id="i-play" viewBox="0 0 24 24"><path d="M7 4l12 8-12 8z" fill="none" stroke="#fff" stroke-width="1.8" stroke-linejoin="round"/></symbol>
    <symbol id="i-sys" viewBox="0 0 60 14"><path d="M2 11h2v2H2z M6 9h2v4H6z M10 6h2v7h-2z M14 3h2v10h-2z" fill="#fff"/><path d="M22 7a8 8 0 0 1 11 0 M24.5 9.5a4.5 4.5 0 0 1 6 0" stroke="#fff" stroke-width="1.6" fill="none"/><circle cx="27.5" cy="12" r="1.3" fill="#fff"/><rect x="38" y="3" width="18" height="9" rx="2.5" fill="#fff"/><rect x="57" y="6" width="1.5" height="3" fill="#fff"/></symbol>
  </defs>
</svg>

<!-- Screen: Home -->
<section class="screen" style="left:249px;top:55px">
  <div class="abs status">9:41</div>
  <svg class="abs status-icons" width="60" height="14"><use href="#i-sys"/></svg>
  <div class="abs avatar" role="img" aria-label="Profile photo of John"></div>
  <div class="abs greet">Hi, <b>JOHN</b><div class="sub">CHECK YOUR CHALLANGES</div></div>
  <div class="abs bell"><svg width="22" height="22"><use href="#i-bell"/></svg></div>

  <div class="abs section" style="top:142px"><h2><span class="slash">/</span>THIS WEEK</h2><span class="all">VIEW ALL</span></div>
  <div class="abs hero" style="top:183px">
    <div class="photo runner" role="img" aria-label="Marathon runner in a yellow vest mid-race"></div>
    <h3>Downtown Up &amp;<br>Running II</h3>
    <svg class="trophy" width="24" height="24"><use href="#i-trophy"/></svg>
    <p class="prize">6 month free Iron Den subscription.</p>
    <div class="pill">LIVE STATS<svg width="20" height="20"><use href="#i-bars"/></svg></div>
  </div>
  <div class="abs togo" style="top:359px">
    <svg width="24" height="24" style="color:#fff"><use href="#i-watch"/></svg>
    <span class="big">1.3</span><span class="unit">KM<small>TO GO!</small></span>
    <span class="join">JOIN CHALLENGE</span>
    <span class="circle-btn"><svg width="16" height="16" style="color:#f2d21b"><use href="#i-chev"/></svg></span>
  </div>

  <div class="abs section" style="top:457px"><h2><span class="slash">/</span>UPCOMING</h2><span class="all">VIEW ALL</span></div>
  <div class="abs event" style="top:498px">
    <div class="date soon">19<small>NOV</small></div>
    <div class="info"><h4>Downtown Monthly 6 KM</h4><span class="dist"><svg width="22" height="22"><use href="#i-route"/></svg>6 KM</span><span class="check">CHECK IT OUT<svg width="14" height="14" style="color:#111"><use href="#i-chev"/></svg></span></div>
  </div>
  <div class="abs event" style="top:586px">
    <div class="date">22<small>NOV</small></div>
    <div class="info"><h4>Harbor City winter marathon</h4><span class="dist"><svg width="22" height="22"><use href="#i-route"/></svg>300 M</span><span class="check">CHECK IT OUT<svg width="14" height="14" style="color:#111"><use href="#i-chev"/></svg></span></div>
  </div>
  <div class="abs fab" style="top:673px"><svg width="26" height="26" style="color:#111"><use href="#i-alarm"/></svg></div>
  <div class="abs create" style="top:706px"><span class="plus">+</span>CREATE YOUR OWN!</div>
  <div class="abs clan" style="top:748px">
    <div class="photo crowd" role="img" aria-label="Group of runners racing together"></div>
    <h3>Bring your own clan<br>&amp; run!</h3>
  </div>
  <nav class="abs nav" style="top:746px">
    <span class="tab wide">HOME<svg width="22" height="22" style="color:#f2d21b"><use href="#i-home"/></svg></span>
    <span class="tab"><svg width="22" height="22" style="color:#ccc"><use href="#i-grid"/></svg></span>
    <span class="tab"><svg width="22" height="22" style="color:#ccc"><use href="#i-slide"/></svg></span>
    <span class="tab"><svg width="22" height="22" style="color:#ccc"><use href="#i-alarm"/></svg></span>
  </nav>
</section>

<!-- Screen: Home with live stats -->
<section class="screen" style="left:612px;top:55px">
  <div class="abs status">9:41</div>
  <svg class="abs status-icons" width="60" height="14"><use href="#i-sys"/></svg>
  <div class="abs avatar" role="img" aria-label="Profile photo of John"></div>
  <div class="abs greet">Hi, <b>JOHN</b><div class="sub">CHECK YOUR CHALLANGES</div></div>
  <div class="abs bell"><svg width="22" height="22"><use href="#i-bell"/></svg></div>

  <div class="abs section" style="top:142px"><h2><span class="slash">/</span>THIS WEEK</h2><span class="all">VIEW ALL</span></div>
  <div class="abs hero" style="top:183px">
    <div class="photo runner" role="img" aria-label="Marathon runner in a yellow vest mid-race"></div>
    <h3>Downtown Up &amp;<br>Running II</h3>
    <svg class="trophy" width="24" height="24"><use href="#i-trophy"/></svg>
    <p class="prize">6 month free Iron Den subscription.</p>
    <div class="pill">LIVE STATS<svg width="20" height="20"><use href="#i-close"/></svg></div>
  </div>
  <div class="abs stats" style="top:359px">
    <div class="stat" style="left:30px"><svg width="22" height="22" style="color:#111"><use href="#i-watch"/></svg><div class="n">1.7<sup>KM</sup></div><div class="l">MOST KM</div></div>
    <div class="stat" style="left:147px"><svg width="22" height="22"><use href="#i-gauge"/></svg><div class="n">29<sup>KM/H</sup></div><div class="l">FASTEST PACE</div></div>
    <div class="stat" style="left:265px"><svg width="22" height="22"><use href="#i-ticket"/></svg><div class="n">#96</div><div class="l">RANDOM DRAW</div></div>
  </div>
  <div class="abs togo" style="top:483px">
    <svg width="24" height="24" style="color:#fff"><use href="#i-watch"/></svg>
    <span class="big">1.3</span><span class="unit">KM<small>TO GO!</small></span>
    <span class="join">JOIN CHALLENGE</span>
    <span class="circle-btn"><svg width="16" height="16" style="color:#f2d21b"><use href="#i-chev"/></svg></span>
  </div>

  <div class="abs section" style="top:582px"><h2><span class="slash">/</span>UPCOMING</h2><span class="all">VIEW ALL</span></div>
  <div class="abs event" style="top:622px">
    <div class="date soon">19<small>NOV</small></div>
    <div class="info"><h4>Downtown Monthly 6 KM</h4><span class="dist"><svg width="22" height="22"><use href="#i-route"/></svg>6 KM</span><span class="check">CHECK IT OUT<svg width="14" height="14" style="color:#111"><use href="#i-chev"/></svg></span></div>
  </div>
  <div class="abs event" style="top:710px">
    <div class="date">22<small>NOV</small></div>
    <div class="info"><h4>Harbor City winter marathon</h4></div>
  </div>
  <div class="abs fab" style="top:673px;left:300px"><svg width="26" height="26" style="color:#111"><use href="#i-alarm"/></svg></div>
  <nav class="abs nav">
    <span class="tab wide">HOME<svg width="22" height="22" style="color:#f2d21b"><use href="#i-home"/></svg></span>
    <span class="tab"><svg width="22" height="22" style="color:#ccc"><use href="#i-grid"/></svg></span>
    <span class="tab"><svg width="22" height="22" style="color:#ccc"><use href="#i-slide"/></svg></span>
    <span class="tab"><svg width="22" height="22" style="color:#ccc"><use href="#i-alarm"/></svg></span>
  </nav>
</section>

<!-- Screen: Home full scroll -->
<section class="screen tall" style="left:249px;top:591px">
  <div class="abs status">9:41</div>
  <svg class="abs status-icons" width="60" height="14"><use href="#i-sys"/></svg>
  <div class="abs avatar" role="img" aria-label="Profile photo of John"></div>
  <div class="abs greet">Hi, <b>JOHN</b><div class="sub">CHECK YOUR CHALLANGES</div></div>
  <div class="abs bell"><svg width="22" height="22"><use href="#i-bell"/></svg></div>

  <div class="abs section" style="top:142px"><h2><span class="slash">/</span>THIS WEEK</h2><span class="all">VIEW ALL</span></div>
  <div class="abs hero" style="top:183px">
    <div class="photo runner" role="img" aria-label="Marathon runner in a yellow vest mid-race"></div>
    <h3>Downtown Up &amp;<br>Running II</h3>
    <svg class="trophy" width="24" height="24"><use href="#i-trophy"/></svg>
    <p class="prize">6 month free Iron Den subscription.</p>
    <div class="pill">LIVE STATS<svg width="20" height="20"><use href="#i-bars"/></svg></div>
  </div>
  <div class="abs togo" style="top:359px">
    <svg width="24" height="24" style="color:#fff"><use href="#i-watch"/></svg>
    <span class="big">1.3</span><span class="unit">KM<small>TO GO!</small></span>
    <span class="join">JOIN CHALLENGE</span>
    <span class="circle-btn"><svg width="16" height="16" style="color:#f2d21b"><use href="#i-chev"/></svg></span>
  </div>

  <div class="abs section" style="top:457px"><h2><span class="slash">/</span>UPCOMING</h2><span class="all">VIEW ALL</span></div>
  <div class="abs event" style="top:498px">
    <div class="date soon">19<small>NOV</small></div>
    <div class="info"><h4>Downtown Monthly 6 KM</h4><span class="dist"><svg width="22" height="22"><use href="#i-route"/></svg>6 KM</span><span class="check">CHECK IT OUT<svg width="14" height="14" style="color:#111"><use href="#i-chev"/></svg></span></div>
  </div>
  <div class="abs event" style="top:586px">
    <div class="date">22<small>NOV</small></div>
    <div class="info"><h4>Harbor City winter marathon</h4><span class="dist"><svg width="22" height="22"><use href="#i-route"/></svg>300 M</span><span class="check">CHECK IT OUT<svg width="14" height="14" style="color:#111"><use href="#i-chev"/></svg></span></div>
  </div>
  <div class="abs create" style="top:706px"><span class="plus">+</span>CREATE YOUR OWN!</div>
  <div class="abs clan" style="top:748px">
    <div class="photo crowd" role="img" aria-label="Group of runners racing together"></div>
    <h3>Bring your own clan<br>&amp; run!</h3>
    <span class="prize-tag"><svg width="24" height="24"><use href="#i-trophy"/></svg>PRIZE</span>
    <p class="note">Name your optional prize<br>and customize the event.</p>
    <div class="go">LET'S GO!<svg width="14" height="14" style="color:#111"><use href="#i-chev"/></svg></div>
  </div>
</section>

<!-- Screen: My challenges -->
<section class="screen" style="left:612px;top:591px">
  <div class="abs status">9:41</div>
  <svg class="abs status-icons" width="60" height="14"><use href="#i-sys"/></svg>
  <div class="abs tabs"><span class="past">PAST CHALLENGES</span><span class="current">CURRENT CHALLENGES</span></div>
  <div class="abs filter" style="left:124px;color:var(--yellow)">REMAING<svg width="18" height="18"><use href="#i-hour"/></svg></div>
  <div class="abs filter" style="left:249px">START DATE<svg width="16" height="16"><use href="#i-play"/></svg></div>

  <div class="abs hero" style="top:183px">
    <div class="photo runner" role="img" aria-label="Marathon runner in a yellow vest mid-race"></div>
    <h3>Downtown Up &amp;<br>Running II</h3>
    <svg class="trophy" width="24" height="24"><use href="#i-trophy"/></svg>
    <p class="prize">6 month free Iron Den subscription.</p>
  </div>
  <div class="abs stats" style="top:359px">
    <div class="stat" style="left:30px"><svg width="22" height="22"><use href="#i-route"/></svg><div class="n">3<sup>KM</sup></div><div class="l">TOTAL DISTANCE</div></div>
    <div class="stat" style="left:147px"><svg width="22" height="22"><use href="#i-gauge"/></svg><div class="n">29<sup>KM/H</sup></div><div class="l">AVERAGE SPEED</div></div>
    <div class="stat" style="left:265px"><svg width="22" height="22"><use href="#i-trend"/></svg><div class="n">30<sup>KM/H</sup></div><div class="l">HIGHEST SPEED</div></div>
  </div>
  <div class="abs togo" style="top:483px">
    <svg width="24" height="24" style="color:#fff"><use href="#i-watch"/></svg>
    <span class="big">1.3</span><span class="unit">KM<small>TO GO!</small></span>
    <span class="join">CHALLENGE DETAILS</span>
    <span class="circle-btn"><svg width="16" height="16" style="color:#f2d21b"><use href="#i-chev"/></svg></span>
  </div>

  <div class="abs hero" style="top:587px">
    <div class="photo pair" role="img" aria-label="Two runners racing side by side"></div>
    <h3>Downtown Monthly<br>6 KM</h3>
    <svg class="trophy" width="24" height="24"><use href="#i-trophy"/></svg>
    <p class="prize">1 Year free Iron Den subscription.</p>
  </div>
  <div class="abs stats" style="top:763px">
    <div class="stat" style="left:30px"><svg width="22" height="22"><use href="#i-route"/></svg><div class="n">3<sup>KM</sup></div></div>
    <div class="stat" style="left:147px"><svg width="22" height="22"><use href="#i-gauge"/></svg><div class="n">29<sup>KM/H</sup></div></div>
    <div class="stat" style="left:265px"><svg width="22" height="22"><use href="#i-trend"/></svg><div class="n">30<sup>KM/H</sup></div></div>
  </div>
  <div class="abs fab" style="top:673px;left:300px"><svg width="26" height="26" style="color:#111"><use href="#i-alarm"/></svg></div>
  <nav class="abs nav">
    <span class="tab"><svg width="22" height="22" style="color:#ccc"><use href="#i-home"/></svg></span>
    <span class="tab wide">MY CHALLENGES<svg width="22" height="22" style="color:#f2d21b"><use href="#i-grid"/></svg></span>
    <span class="tab"><svg width="22" height="22" style="color:#ccc"><use href="#i-slide"/></svg></span>
    <span class="tab"><svg width="22" height="22" style="color:#ccc"><use href="#i-alarm"/></svg></span>
  </nav>
</section>

</body>
</html>
```